Collectibles expert needs a new business card design.

My current business card makes me look to high end. It may even make me look arrogant or too stuffy. I do work with high end clients and their items but most of my business is with average people with average items. My business name is Walter Brumby's Old Mill Digging Co. The idea was that I mine the streets helping people discover the treasures buried in their homes. That could be art, jewelry, coins, etc. The name and an older logo I used does not make immediate sense to most people. I tried to go with just my picture and name and that is the current card I am changing. I help people who need to downsize. Whether they are getting rid of one item, a collection or a house full of items I help them discover what they have, what it is worth and what are the best ways we can get the most for them. This may be a combination of estate sale (which I dont do) auction or sell directly to a dealer or collector. Usually it is a combination of these. My main goal is to help make sure they dont accidently sell a Vandermeer painting in a garage sale. I am uploading a copy of my old card and the old logo I used to use but the winning card design will need to be much different than these. You can learn a little more about me at www.walterkbrumby.example, www.oldmilldigng.example and www.facebook.com/omdco. I hope someone can look at what I do and come up with a very unique design that will be equally effective if my client is high income or if my client is low to mid income. I do not care if it is a one or two sided card as long as it conveys my contact information and a good representation of what I do.

Target Market(s)

People who are getting rid of items. These can be elderly couples or individuals that are moving to an active living community and will have less space so they need to sell items. This can also include the children of elder parents that dont want their stuff and want to find solutions to help them get rid of their items.

Contact Information for Business Card

The card should have my business name Walter Brumby's Old Mill Digging Co., phone number 555-312-70981, email walter@oldmilldigging.example and website www.oldmilldigging.example. Would also like to include Buyer, Broker, Consultant and Appraiser. We can put Walter K. Brumby, ISA on the opposite side of the company name since it includes my name as well.

Font styles to use
Sans Serif

Colors

Designer to choose colors to be used in the design.

Requirements
Must have
• My project must have a professional look. It must not alienate low income clients and should still be appealing to high value clients.

```html
<!DOCTYPE html>
<html lang="en">
<head>
<meta charset="utf-8">
<title>Walter Brumby's Old Mill Digging Co. — Business Card</title>
<link rel="stylesheet" href="https://fonts.googleapis.com/css2?family=Bebas+Neue&family=Lato:wght@400;700&display=swap">
<style>
  :root {
    --backdrop: #e6e3df;
    --card-white: #ffffff;
    --card-shade: #f1f1f1;
    --copper: #b5724a;
    --copper-deep: #93593a;
    --copper-light: #c07e55;
    --ink-brown: #4a2218;
    --accent-orange: #c0724a;
    --divider: #6b3a28;
    --art-blue: #6f93b4;
    --art-red: #6a1f1c;
  }
  * { box-sizing: border-box; margin: 0; padding: 0; }
  html, body { width: 1200px; height: 900px; overflow: hidden; }
  body {
    background: var(--backdrop);
    display: flex;
    flex-direction: column;
    align-items: center;
    justify-content: center;
    gap: 36px;
  }
  .card {
    width: 700px;
    height: 400px;
    border-radius: 22px;
    position: relative;
    overflow: hidden;
    box-shadow: 0 8px 24px rgba(0,0,0,0.18);
  }
  /* Front side */
  .card-front {
    background: radial-gradient(ellipse at 45% 55%, var(--card-white) 40%, var(--card-shade) 100%);
    display: flex;
    align-items: center;
    padding-left: 62px;
  }
  .identity {
    display: flex;
    flex-direction: column;
    align-items: flex-end;
  }
  .owner-name {
    font-family: "Bebas Neue", "Oswald", sans-serif;
    font-size: 50px;
    letter-spacing: 2px;
    color: var(--accent-orange);
    line-height: 1;
  }
  .owner-roles {
    font-family: "Lato", sans-serif;
    font-size: 17px;
    color: var(--ink-brown);
    margin-top: 6px;
  }
  .divider {
    width: 2px;
    height: 76px;
    background: var(--divider);
    margin: 0 24px 0 26px;
  }
  .contact-list {
    list-style: none;
    font-family: "Lato", sans-serif;
    font-size: 16.5px;
    color: var(--ink-brown);
    display: flex;
    flex-direction: column;
    gap: 6px;
  }
  .contact-list li {
    display: flex;
    align-items: center;
    gap: 9px;
  }
  .contact-icon { width: 12px; height: 12px; flex: none; }
  /* Back side */
  .card-back {
    background: linear-gradient(135deg, var(--copper-light) 0%, var(--copper) 50%, var(--copper-deep) 100%);
  }
  .mascot-art {
    position: absolute;
    right: 40px;
    top: 34px;
    width: 300px;
    height: 330px;
    border-radius: 30px;
    background: linear-gradient(160deg, var(--art-blue) 0%, #5a6f86 45%, var(--art-red) 100%);
    opacity: 0.9;
  }
</style>
</head>
<body>
  <section class="card card-front" aria-label="Card front">
    <div class="identity">
      <h1 class="owner-name">Walter Brumby's</h1>
      <p class="owner-roles">Buyer, Broker, Consultant</p>
    </div>
    <div class="divider"></div>
    <ul class="contact-list">
      <li>
        <svg class="contact-icon" viewBox="0 0 12 12" aria-hidden="true"><path d="M3 1 L5 3.5 L4 5 Q5 7 7 8 L8.5 7 L11 9 L9.5 11 Q4 10.5 1 2.5 Z" fill="var(--accent-orange)"/></svg>
        <span>555-312-70981,</span>
      </li>
      <li>
        <svg class="contact-icon" viewBox="0 0 12 12" aria-hidden="true"><rect x="1" y="2.5" width="10" height="7" fill="none" stroke="var(--accent-orange)" stroke-width="1.2"/><path d="M1 2.5 L6 6.5 L11 2.5" fill="none" stroke="var(--accent-orange)" stroke-width="1.2"/></svg>
        <span>walter@oldmilldigging.example</span>
      </li>
      <li>
        <svg class="contact-icon" viewBox="0 0 12 12" aria-hidden="true"><circle cx="6" cy="6" r="5" fill="none" stroke="var(--accent-orange)" stroke-width="1.2"/><ellipse cx="6" cy="6" rx="2.2" ry="5" fill="none" stroke="var(--accent-orange)" stroke-width="1"/><path d="M1 6 H11" stroke="var(--accent-orange)" stroke-width="1"/></svg>
        <span>www.oldmilldigging.example</span>
      </li>
    </ul>
  </section>

  <section class="card card-back" aria-label="Card back">
    <div class="mascot-art" role="img" aria-label="Painted illustration of a woman miner in blue work clothes holding a pickaxe, seated on a red mine cart filled with gold"></div>
  </section>
</body>
</html>
```